Project Manager Business Card for Top Architectural Firm

Update and design a stunning Senior Project Manager Business Card

MARCO T. RUEDA II
Senior Project Manager

H A R B O R L I N E
A R C H I T E C T U R E L L C.
www.HarborlineCrestHouses.com
4217 NW 38th Ter. Suite 905
Miami, FL 33172
C: (305) 418-2273
mrueda.harborlinecresthouses@mailvista.net

Looking to have the logo to be UV Spot ink printed and to be prominent.

Target Market(s)

High end real estate architecture construction

Industry/Entity Type

Architect

Contact Information for Business Card

MARCO T. RUEDA II
Senior Project Manager

H A R B O R L I N E
Miami, FL 33172
C: (305) 418-2273

Font styles to use
Sans Serif

Colors

Designer to choose colors to be used in the design.

Requirements
Must have
• Prominent Logo

```html
<!DOCTYPE html>
<html lang="en">
<head>
<meta charset="utf-8">
<title>Harborline Architecture – Business Card</title>
<link rel="stylesheet" href="https://fonts.googleapis.com/css2?family=Arimo:wght@400;700&display=swap">
<style>
  :root {
    --page-bg: #d8d4cf;
    --card-top: #f3f4f5;
    --card-bottom: #e4e8eb;
    --brand-blue: #2a7fb0;
    --brand-blue-deep: #1b6796;
    --ink: #2b2b2e;
    --ink-soft: #4a4a4f;
    --swoosh: #26262a;
    --copper: #c98f7f;
    --web-text: #d9c9c6;
  }
  * { margin: 0; padding: 0; box-sizing: border-box; }
  html, body { width: 1200px; height: 970px; overflow: hidden; }
  body {
    background: var(--page-bg);
    font-family: "Arimo", Arial, sans-serif;
    position: relative;
  }
  .card {
    position: absolute;
    left: 100px; top: 185px;
    width: 1000px; height: 600px;
    background: linear-gradient(180deg, var(--card-top), var(--card-bottom));
    overflow: hidden;
    box-shadow: 0 10px 30px rgba(0,0,0,0.18);
  }
  .card-art { position: absolute; inset: 0; }
  .brand {
    position: absolute; left: 43px; top: 62px;
    color: var(--ink);
    font-weight: 400;
  }
  .brand-dot {
    width: 118px; height: 118px; border-radius: 50%;
    background: var(--brand-blue);
    margin-left: 40px; margin-bottom: 28px;
  }
  .brand-name {
    font-size: 34px; letter-spacing: 8px; line-height: 1;
  }
  .brand-sub {
    font-size: 11px; letter-spacing: 4.2px; margin-top: 8px;
  }
  .contact {
    position: absolute; right: 24px; top: 100px;
    text-align: right;
  }
  .contact-name {
    color: var(--brand-blue); font-weight: 700; font-size: 23px; letter-spacing: 0.5px;
  }
  .contact-title { color: var(--ink); font-size: 22px; margin-top: 8px; }
  .contact-line {
    display: flex; justify-content: flex-end; align-items: center;
    color: var(--ink); font-size: 21px; margin-top: 14px; gap: 10px;
  }
  .contact-icon { width: 26px; height: 26px; flex: none; }
  .address {
    position: absolute; left: 43px; top: 402px;
    color: var(--ink-soft); font-size: 22px; line-height: 37px;
  }
  .address-company { color: var(--brand-blue); font-weight: 700; font-size: 22px; letter-spacing: 0.4px; }
  .website {
    position: absolute; right: 24px; top: 543px;
    color: var(--web-text); font-weight: 700; font-size: 22px;
  }
</style>
</head>
<body>
  <div class="card">
    <svg class="card-art" viewBox="0 0 1000 600" width="1000" height="600" aria-hidden="true">
      <defs>
        <linearGradient id="bandFill" x1="0" y1="1" x2="1" y2="0">
          <stop offset="0" stop-color="#1e6f9f"/>
          <stop offset="1" stop-color="#2b8fc0"/>
        </linearGradient>
      </defs>
      <path d="M0,600 L0,545 C320,505 700,430 1000,330 L1000,600 Z" fill="url(#bandFill)"/>
      <path d="M0,582 C230,548 470,512 690,470 C480,520 250,560 0,598 Z" fill="var(--copper)" opacity="0.7"/>
      <path d="M0,562 C210,528 450,500 690,468 C460,512 240,548 0,586 Z" fill="var(--swoosh)"/>
      <circle cx="848" cy="425" r="93" fill="none" stroke="var(--brand-blue-deep)" stroke-width="3"/>
    </svg>

    <div class="brand">
      <div class="brand-dot"></div>
      <div class="brand-name">HARBORLINE</div>
      <div class="brand-sub">ARCHITECTURE LLC.</div>
    </div>

    <div class="contact">
      <div class="contact-name">MARCO T. RUEDA II</div>
      <div class="contact-title">Senior Project Manager</div>
      <div class="contact-line">
        <span>(305) 418-2273</span>
        <svg class="contact-icon" viewBox="0 0 26 26" aria-hidden="true">
          <circle cx="13" cy="13" r="13" fill="var(--brand-blue)"/>
          <path d="M7,15 C7,10 19,10 19,15 L16.5,15 L16,13 L10,13 L9.5,15 Z M9,16 L17,16 L18,19 L8,19 Z" fill="#fff"/>
        </svg>
      </div>
      <div class="contact-line">
        <span>mrueda.harborlinecresthouses@mailvista.net</span>
        <svg class="contact-icon" viewBox="0 0 26 26" aria-hidden="true">
          <circle cx="13" cy="13" r="13" fill="var(--brand-blue)"/>
          <rect x="7" y="9" width="12" height="8" fill="none" stroke="#fff" stroke-width="1.5"/>
          <path d="M7,9 L13,14 L19,9" fill="none" stroke="#fff" stroke-width="1.5"/>
        </svg>
      </div>
    </div>

    <div class="address">
      <div class="address-company">HARBORLINE ARCHITECTURE LLC.</div>
      <div>4217 NW 38th Ter. Suite 905</div>
      <div>Miami, FL 33172</div>
    </div>

    <div class="website">www.HarborlineCrestHouses.com</div>
  </div>
</body>
</html>
```